International online gaming platform needs a game UI design

1. We need a game interface for three kinds of theme based on our guideline and sample mockup.
2. The product type is the online casino games related, we need a series of casino games UIs, however, we can start on the game lobby first.
3. Three theme you might choose from or refer to:
A. 3D look & feel
B. Realistic casino theme
C. Richness and grandeur
D. European casino style
4. NOT ALLOWED to change the design layout.
MUST follow our sample mock up and ONLY redefine the design style.
5. All items must be in a stand-alone component, eg. Button, Tab, Icon,... etc.
6. We need the layout in vector shape, but we can review in JPG or PNG format.
7. The image size: 1366 x 768

Updated:
1. All items and their positions should be same as the sample UI we provided.
Please redesign all the items and create a new theme for it.
No need to create a new layout.
2. Although we accept the draft design, but all the items in UI should be completed.
3. All the wordings in the sample UI are confirmed, you might change the fonts.
4. For the avatar in the left hand side, you don't have to redraw it.
We already have our own avatar system implemented.
5. All the items such as icons, tabs, and buttons are free to redesign.

Dear designers,

We've increased our budget and raise the prize money to 800 USD.  
We also accept the draft design in PNG format and we can go through the details in handover stage.
Thank you very much. 

Reason: Dear designers, We decided to extend the deadline by 7 days. As mentioned in the task description, we are looking for a new style of design and you might refer to the below style. A. 3D look & feel B. Realistic casino theme C. Richness and grandeur D. European casino style If you are still interested in our project, please send us your work. Thank you very much!

```html
<!DOCTYPE html>
<html lang="en">
<head>
<meta charset="utf-8">
<title>Live Casino Lobby</title>
<link href="https://fonts.googleapis.com/css2?family=Roboto:ital,wght@0,400;0,500;0,700;0,900;1,700;1,900&family=Roboto+Condensed:wght@400;700&display=swap" rel="stylesheet">
<style>
:root{
  --ink:#0d0b08;
  --bar-top:#2c2b29;
  --bar-bot:#0f0f0e;
  --gold-hi:#f6e3a0;
  --gold:#d8b35c;
  --gold-mid:#b8903e;
  --gold-dk:#7a5a22;
  --brown:#4a3413;
  --brown-dk:#2e2109;
  --panel:#8a6a2c;
  --red:#b8230f;
  --red-dk:#7a1306;
  --red-hi:#e0452a;
  --orange:#c9772a;
  --orange-dk:#a25a1c;
  --felt:#17363a;
  --felt-dk:#0d2326;
  --cream:#fff7dc;
  --blue:#1e5f8e;
  --blue-dk:#0b2b46;
  --text-gold:#ffd36b;
}
*{box-sizing:border-box;margin:0;padding:0}
html,body{width:1200px;height:675px;overflow:hidden;background:var(--ink)}
body{font-family:"Roboto",Arial,sans-serif;color:var(--cream)}
.lobby{position:relative;width:1200px;height:675px;overflow:hidden;background:linear-gradient(#3a3935,#1a1917)}
.abs{position:absolute}
svg.defs{position:absolute;width:0;height:0}

/* top bar */
.topbar{left:0;top:0;width:1200px;height:38px;background:linear-gradient(var(--bar-top),var(--bar-bot));border-bottom:2px solid var(--gold-dk)}
.brand{left:0;top:0;width:305px;height:38px;background:linear-gradient(100deg,var(--red) 0%,var(--red-dk) 85%,transparent 86%);display:flex;align-items:center;gap:8px;padding-left:12px;border-bottom:2px solid var(--gold)}
.brand-dot{width:22px;height:22px;border-radius:50%;background:var(--gold)}
.brand-name{font-weight:900;font-size:28px;letter-spacing:1px;color:var(--gold-hi)}
.tools{right:10px;top:4px;display:flex;gap:9px}
.tool{width:36px;height:30px;border-radius:4px;background:linear-gradient(var(--gold-hi),var(--gold-mid));border:1px solid var(--gold-dk);display:flex;align-items:center;justify-content:center}
.tool svg{width:20px;height:20px}
.tool.close{background:linear-gradient(var(--red-hi),var(--red-dk))}

/* sidebar */
.sidebar{left:0;top:38px;width:188px;height:600px;background:linear-gradient(90deg,var(--gold-mid),var(--gold-hi) 40%,var(--gold) 100%);border-right:2px solid var(--gold-dk)}
.clock{left:14px;top:14px;width:158px;height:30px;border:1px solid var(--gold-dk);border-radius:4px;background:linear-gradient(var(--gold-hi),var(--gold));font-size:10px;color:var(--brown-dk);display:flex;align-items:center;justify-content:center}
.profile{left:16px;top:57px;width:156px;height:178px;border:2px solid var(--gold-dk);border-radius:4px;background:var(--gold-hi)}
.avatar{position:absolute;left:4px;top:4px;width:144px;height:142px;background:radial-gradient(circle at 50% 45%,#e8e4dc 0 18%,transparent 19%),linear-gradient(var(--blue),var(--blue-dk))}
.username{position:absolute;left:0;bottom:2px;width:100%;height:26px;display:flex;align-items:center;justify-content:center;gap:14px;font-size:12px;color:var(--brown);padding-left:10px}
.username svg{width:15px;height:15px}
.knob{left:75px;top:244px;width:38px;height:38px;border-radius:50%;background:radial-gradient(circle at 40% 35%,var(--gold-hi),var(--gold-mid) 60%,var(--gold-dk));border:2px solid var(--brown)}
.menu{left:16px;top:262px;width:156px;height:328px;background:linear-gradient(var(--orange),var(--orange-dk));border:2px solid var(--gold-dk);border-radius:4px}
.menu-btn{position:absolute;left:10px;width:132px;height:31px;border:1px solid var(--gold-mid);border-radius:3px;background:linear-gradient(var(--orange),var(--orange-dk));font-size:11px;font-weight:500;color:var(--cream);display:flex;align-items:center;gap:5px;padding-left:6px}
.menu-btn svg{width:16px;height:16px}

/* tabs */
.tab{top:43px;height:49px;border:2px solid var(--gold);background:linear-gradient(var(--red),var(--red-dk));display:flex;align-items:center;gap:10px;padding-left:12px;font-weight:700;font-style:italic;font-size:20px;color:var(--gold-hi);box-shadow:inset 0 0 0 3px var(--red-dk),inset 0 0 0 4px var(--gold-mid)}
.tab.active{background:linear-gradient(var(--gold-hi),var(--gold-mid));color:var(--red-dk);box-shadow:inset 0 0 0 3px var(--gold-mid),inset 0 0 0 4px var(--gold-dk)}
.tab-icon{width:38px;height:32px;border-radius:4px;background:linear-gradient(var(--gold-hi),var(--gold-dk))}
.tab.active .tab-icon{background:linear-gradient(var(--red-hi),var(--red-dk))}

/* main panel */
.main{left:198px;top:98px;width:992px;height:526px;background:linear-gradient(var(--panel),#6d5221);border:2px solid var(--gold-dk);border-radius:4px}
.dealer{position:absolute;background:linear-gradient(var(--gold-hi),var(--gold));border:2px solid var(--gold-dk);border-radius:3px}
.dealer-photo{position:absolute;background:radial-gradient(ellipse at 50% 60%,#082238 0 30%,transparent 31%),linear-gradient(var(--blue),var(--blue-dk));border:2px solid var(--brown)}
.roadmap{position:absolute;background:#fff;border:1px solid var(--gold-dk)}
.roadmap svg{width:100%;height:100%;display:block}
.dealer-bar{position:absolute;left:0;bottom:0;width:100%;display:flex;font-style:italic;font-weight:700;color:var(--brown)}
.dealer-bar .name{flex:1;display:flex;align-items:center;padding-left:6px;background:linear-gradient(var(--gold),var(--gold-mid))}
.dealer-bar .deals{display:flex;align-items:center;justify-content:center;background:linear-gradient(var(--red),var(--red-dk));color:var(--cream)}

/* filter row */
.filters{left:12px;top:140px}
.btn-gold{position:absolute;top:0;height:34px;border:1px solid var(--gold-dk);border-radius:4px;background:linear-gradient(var(--gold-hi),var(--gold-mid));color:var(--brown-dk);font-size:12px;font-weight:500;display:flex;align-items:center;justify-content:center;gap:6px}
.btn-gold svg{width:18px;height:18px}
.filter-track{position:absolute;top:0;left:160px;width:232px;height:34px;background:linear-gradient(#5a4217,#3a2a0c);border:1px solid var(--gold-dk);border-radius:0 4px 4px 0}
.btn-red{background:linear-gradient(var(--red),var(--red-dk));color:var(--cream);font-size:14px;border-color:var(--gold)}

/* tables */
.tables{left:12px;top:196px;display:grid;grid-template-columns:repeat(3,306px);grid-auto-rows:151px;column-gap:11px;row-gap:12px}
.table-card{position:relative;border:2px solid var(--gold);border-radius:4px;background:linear-gradient(var(--brown),var(--brown-dk))}
.table-head{position:absolute;left:0;top:0;width:100%;height:40px;padding:3px 7px;font-size:10.5px;display:flex;justify-content:space-between;background:linear-gradient(#5a3f16,#3a2a0c)}
.table-head .name,.table-head .comm{color:var(--text-gold)}
.table-head .limit,.table-head .seats{color:#fff}
.table-head .right{text-align:right}
.join{position:absolute;left:115px;top:-9px;width:74px;height:62px;border-radius:50%;background:radial-gradient(ellipse at 45% 35%,var(--gold-hi),var(--gold) 55%,var(--gold-dk));border:2px solid var(--brown);box-shadow:0 0 0 2px var(--gold);display:flex;align-items:center;justify-content:center;color:var(--red);font-size:14px;font-weight:700}
.felt{position:absolute;left:6px;top:52px;width:290px;height:52px}
.seat-row{position:absolute;left:3px;top:112px;display:flex;gap:5px}
.seat{width:38px;height:30px;border-radius:3px;border:1px solid var(--gold-dk);background:linear-gradient(var(--gold-hi),var(--gold-mid));display:flex;align-items:center;justify-content:center}
.seat svg{width:20px;height:20px}
.seat.down{background:linear-gradient(var(--red-hi),var(--red-dk))}
.scroll{left:966px;top:194px;width:12px;height:316px;border-radius:6px;background:var(--brown-dk);border:1px solid var(--gold-dk)}
.scroll-thumb{position:absolute;left:-3px;top:-2px;width:16px;height:18px;border-radius:50%;background:radial-gradient(circle at 40% 35%,var(--gold-hi),var(--gold-dk))}

/* bottom bar */
.bottombar{left:0;top:638px;width:1200px;height:37px;background:linear-gradient(var(--bar-top),var(--bar-bot));border-top:2px solid var(--gold-dk)}
.balance{right:10px;top:4px;display:flex;height:28px;border:1px solid var(--gold-dk);border-radius:4px;overflow:hidden;font-size:13px;font-weight:700}
.balance .label{width:72px;background:linear-gradient(var(--gold-hi),var(--gold-mid));color:var(--brown-dk);display:flex;align-items:center;justify-content:center}
.balance .cur{width:56px;background:linear-gradient(var(--gold),var(--gold-dk));color:var(--brown-dk);display:flex;align-items:center;justify-content:center;border-left:2px solid var(--brown)}
.balance .amount{width:124px;background:linear-gradient(var(--red),var(--red-dk));color:var(--gold-hi);display:flex;align-items:center;justify-content:center;border-left:2px solid var(--brown)}
</style>
</head>
<body>
<svg class="defs" aria-hidden="true">
  <defs>
    <symbol id="person" viewBox="0 0 20 20"><circle cx="10" cy="6" r="4" fill="#4a3413"/><path d="M3 19c0-5 3-8 7-8s7 3 7 8z" fill="#4a3413"/></symbol>
    <symbol id="arrow-down" viewBox="0 0 20 20"><path d="M8 2h4v9h4l-6 7-6-7h4z" fill="#fff7dc"/></symbol>
    <symbol id="felt" viewBox="0 0 300 54">
      <polygon points="22,2 278,2 298,52 2,52" fill="#17363a"/>
      <g stroke="#e9f1ee" stroke-width="1" fill="none">
        <line x1="16" y1="6" x2="284" y2="6"/>
        <line x1="12" y1="16" x2="288" y2="16"/>
        <line x1="8" y1="28" x2="292" y2="28"/>
        <line x1="2" y1="52" x2="298" y2="52"/>
        <line x1="16" y1="6" x2="2" y2="52"/><line x1="284" y1="6" x2="298" y2="52"/>
        <line x1="54" y1="6" x2="44" y2="52"/><line x1="92" y1="6" x2="86" y2="52"/>
        <line x1="130" y1="6" x2="128" y2="52"/><line x1="168" y1="6" x2="170" y2="52"/>
        <line x1="206" y1="6" x2="212" y2="52"/><line x1="245" y1="6" x2="255" y2="52"/>
      </g>
      <g font-family="Georgia,serif" font-style="italic" font-size="10" fill="#e6c35b" text-anchor="middle">
        <text x="33" y="26">B</text><text x="71" y="26">B</text><text x="109" y="26">B</text><text x="148" y="26">B</text><text x="187" y="26">B</text><text x="226" y="26">B</text><text x="266" y="26">B</text>
      </g>
      <g font-family="Georgia,serif" font-style="italic" font-size="15" fill="#fff" text-anchor="middle">
        <text x="26" y="46">P</text><text x="66" y="46">P</text><text x="107" y="46">P</text><text x="148" y="46">P</text><text x="190" y="46">P</text><text x="232" y="46">P</text><text x="273" y="46">P</text>
      </g>
    </symbol>
    <symbol id="road" viewBox="0 0 144 64" preserveAspectRatio="none">
      <g stroke="#c9c9c9" stroke-width=".6">
        <path d="M12 0v64M24 0v64M36 0v64M48 0v64M60 0v64M72 0v64M84 0v64M96 0v64M108 0v64M120 0v64M132 0v64"/>
        <path d="M0 10.7h144M0 21.3h144M0 32h144M0 42.7h144M0 53.3h144"/>
      </g>
      <g fill="none" stroke-width="1.6">
        <circle cx="6" cy="5.3" r="3.6" stroke="#c8a238"/><circle cx="18" cy="5.3" r="3.6" stroke="#c81e1e"/><circle cx="18" cy="16" r="3.6" stroke="#c81e1e"/>
        <circle cx="30" cy="5.3" r="3.6" stroke="#c8a238"/><circle cx="42" cy="5.3" r="3.6" stroke="#c81e1e"/><circle cx="54" cy="5.3" r="3.6" stroke="#c8a238"/>
        <circle cx="54" cy="16" r="3.6" stroke="#c8a238"/><circle cx="66" cy="5.3" r="3.6" stroke="#c81e1e"/><circle cx="78" cy="5.3" r="3.6" stroke="#c8a238"/>
        <circle cx="90" cy="5.3" r="3.6" stroke="#c8a238"/><circle cx="90" cy="16" r="3.6" stroke="#c8a238"/><circle cx="90" cy="26.7" r="3.6" stroke="#c8a238"/>
        <circle cx="102" cy="5.3" r="3.6" stroke="#c81e1e"/><circle cx="114" cy="5.3" r="3.6" stroke="#c8a238"/><circle cx="114" cy="16" r="3.6" stroke="#c8a238"/>
        <circle cx="126" cy="5.3" r="3.6" stroke="#c81e1e"/><circle cx="126" cy="16" r="3.6" stroke="#c81e1e"/><circle cx="126" cy="26.7" r="3.6" stroke="#c81e1e"/>
        <circle cx="126" cy="37.3" r="3.6" stroke="#c81e1e"/><circle cx="126" cy="48" r="3.6" stroke="#c81e1e"/>
      </g>
    </symbol>
  </defs>
</svg>

<div class="lobby">
  <header class="topbar abs">
    <div class="brand abs"><span class="brand-dot"></span><span class="brand-name">LIVE CASINO</span></div>
    <nav class="tools abs">
      <span class="tool"><svg viewBox="0 0 20 20"><rect x="2" y="4" width="16" height="11" rx="1" fill="none" stroke="#4a3413" stroke-width="2"/><path d="M7 18h6" stroke="#4a3413" stroke-width="2"/></svg></span>
      <span class="tool"><svg viewBox="0 0 20 20"><circle cx="8" cy="8" r="5.5" fill="none" stroke="#4a3413" stroke-width="2"/><path d="M12 12l6 6M5 8h6M8 5v6" stroke="#4a3413" stroke-width="2"/></svg></span>
      <span class="tool"><svg viewBox="0 0 20 20"><circle cx="8" cy="8" r="5.5" fill="none" stroke="#4a3413" stroke-width="2"/><path d="M12 12l6 6M5 8h6" stroke="#4a3413" stroke-width="2"/></svg></span>
      <span class="tool"><svg viewBox="0 0 20 20"><path d="M7 15V4l10-2v11" fill="none" stroke="#4a3413" stroke-width="2"/><circle cx="5" cy="15" r="2.5" fill="#4a3413"/><circle cx="15" cy="13" r="2.5" fill="#4a3413"/></svg></span>
      <span class="tool"><svg viewBox="0 0 20 20"><path d="M2 7V2h5M13 2h5v5M18 13v5h-5M7 18H2v-5" fill="none" stroke="#4a3413" stroke-width="2"/><rect x="7" y="7" width="6" height="6" fill="#4a3413"/></svg></span>
      <span class="tool close"><svg viewBox="0 0 20 20"><circle cx="10" cy="10" r="7" fill="none" stroke="#fff7dc" stroke-width="2"/><path d="M7 7l6 6M13 7l-6 6" stroke="#fff7dc" stroke-width="2"/></svg></span>
    </nav>
  </header>

  <aside class="sidebar abs">
    <div class="clock abs">1/28/2014 &nbsp;06:54 &nbsp;PM GMT+8</div>
    <div class="profile abs">
      <div class="avatar" role="img" aria-label="Player avatar"></div>
      <div class="username">ALLos848767 <svg viewBox="0 0 16 16"><rect x="1" y="3" width="11" height="11" fill="none" stroke="#4a3413" stroke-width="1.5"/><path d="M6 10l1-3 7-6 2 2-7 6z" fill="#4a3413"/></svg></div>
    </div>
    <div class="menu abs">
      <div class="menu-btn" style="top:32px"><svg viewBox="0 0 16 16"><path d="M2 3h12v8H7l-4 3v-3H2z" fill="#5a3410"/></svg>Announcements</div>
      <div class="menu-btn" style="top:72px"><svg viewBox="0 0 16 16"><rect x="3" y="1" width="10" height="14" rx="1" fill="none" stroke="#5a3410" stroke-width="1.5"/><path d="M8 4v5M8 11v1.5" stroke="#5a3410" stroke-width="1.8"/></svg>Rules &amp; regulations</div>
      <div class="menu-btn" style="top:112px"><svg viewBox="0 0 16 16"><rect x="1" y="2" width="14" height="9" fill="none" stroke="#5a3410" stroke-width="1.5"/><path d="M5 14h6M8 11v3" stroke="#5a3410" stroke-width="1.5"/></svg>Quick tour</div>
    </div>
    <div class="knob abs"></div>
  </aside>

  <div class="tab active abs" style="left:200px;width:232px"><span class="tab-icon" role="img" aria-label="Playing cards icon"></span>Bacarat</div>
  <div class="tab abs" style="left:443px;width:219px"><span class="tab-icon" role="img" aria-label="Casino chips icon"></span>Super Six</div>
  <div class="tab abs" style="left:678px;width:219px"><span class="tab-icon" role="img" aria-label="Roulette wheel icon"></span>Roulette</div>
  <div class="tab abs" style="left:913px;width:220px"><span class="tab-icon" role="img" aria-label="Dice icon"></span>Sic Bo</div>

  <main class="main abs">
    <div class="dealer" style="left:7px;top:5px;width:274px;height:124px">
      <div class="dealer-photo" role="img" aria-label="Dealer photo" style="left:10px;top:12px;width:84px;height:72px"></div>
      <div class="roadmap" style="left:102px;top:11px;width:162px;height:76px"><svg><use href="#road"/></svg></div>
      <div class="dealer-bar" style="height:28px;font-size:12px"><span class="name">Dealer: Name</span><span class="deals" style="width:80px">Deals 999</span></div>
    </div>
    <div class="dealer" style="left:302px;top:20px;width:218px;height:94px">
      <div class="dealer-photo" role="img" aria-label="Dealer photo" style="left:6px;top:5px;width:70px;height:60px"></div>
      <div class="roadmap" style="left:80px;top:4px;width:132px;height:62px"><svg><use href="#road"/></svg></div>
      <div class="dealer-bar" style="height:22px;font-size:10px"><span class="name">Dealer: Name</span><span class="deals" style="width:64px">Deals 999</span></div>
    </div>
    <div class="dealer" style="left:528px;top:20px;width:218px;height:94px">
      <div class="dealer-photo" role="img" aria-label="Dealer photo" style="left:6px;top:5px;width:70px;height:60px"></div>
      <div class="roadmap" style="left:80px;top:4px;width:132px;height:62px"><svg><use href="#road"/></svg></div>
      <div class="dealer-bar" style="height:22px;font-size:10px"><span class="name">Dealer: Name</span><span class="deals" style="width:64px">Deals 999</span></div>
    </div>
    <div class="dealer" style="left:754px;top:20px;width:218px;height:94px">
      <div class="dealer-photo" role="img" aria-label="Dealer photo" style="left:6px;top:5px;width:70px;height:60px"></div>
      <div class="roadmap" style="left:80px;top:4px;width:132px;height:62px"><svg><use href="#road"/></svg></div>
      <div class="dealer-bar" style="height:22px;font-size:10px"><span class="name">Dealer: Name</span><span class="deals" style="width:64px">Deals 999</span></div>
    </div>

    <div class="filters abs">
      <div class="btn-gold" style="left:0;width:158px"><svg viewBox="0 0 20 20"><use href="#person"/></svg>&nbsp;&nbsp;Multi-player</div>
      <div class="filter-track"></div>
      <div class="btn-gold btn-red" style="left:404px;width:158px"><svg viewBox="0 0 20 20"><circle cx="10" cy="10" r="8" fill="none" stroke="#fff7dc" stroke-width="1.5"/><path d="M6 10l3 3 5-6" fill="none" stroke="#fff7dc" stroke-width="1.8"/></svg>&nbsp;&nbsp;JOIN ANY</div>
      <div class="btn-gold" style="left:567px;width:41px;font-size:11px">A→Z</div>
      <div class="btn-gold" style="left:613px;width:41px">$<svg viewBox="0 0 20 20" style="width:12px"><use href="#arrow-down"/></svg></div>
      <div class="btn-gold" style="left:659px;width:42px">$<svg viewBox="0 0 20 20" style="width:12px;transform:rotate(180deg)"><use href="#arrow-down"/></svg></div>
      <div class="btn-gold" style="left:711px;width:42px"><svg viewBox="0 0 20 20" style="width:26px"><use href="#person"/></svg></div>
      <div class="btn-gold" style="left:759px;width:41px;font-size:13px">≫3</div>
      <div class="btn-gold" style="left:805px;width:41px;font-size:13px">≫3</div>
      <div class="btn-gold" style="left:852px;width:108px"><svg viewBox="0 0 20 20"><path d="M10 1l2.6 6 6.4.5-4.9 4.2 1.5 6.3L10 14.6 4.4 18l1.5-6.3L1 7.5 7.4 7z" fill="#4a3413"/></svg>All limits</div>
    </div>

    <section class="tables abs">
      <article class="table-card">
        <div class="table-head"><div><div class="name">Baccarat A5-3C</div><div class="limit">Bet Limit</div></div><div class="right"><div class="comm">Commission 0/7</div><div class="seats">0/100</div></div></div>
        <div class="join">JOIN</div>
        <svg class="felt" viewBox="0 0 300 54"><use href="#felt"/></svg>
        <div class="seat-row"><span class="seat"><svg><use href="#person"/></svg></span><span class="seat"><svg><use href="#person"/></svg></span><span class="seat"><svg><use href="#person"/></svg></span><span class="seat"><svg><use href="#person"/></svg></span><span class="seat"><svg><use href="#person"/></svg></span><span class="seat down"><svg><use href="#arrow-down"/></svg></span><span class="seat down"><svg><use href="#arrow-down"/></svg></span></div>
      </article>
      <article class="table-card">
        <div class="table-head"><div><div class="name">Baccarat A5-3C</div><div class="limit">Bet Limit</div></div><div class="right"><div class="comm">Commission 0/7</div><div class="seats">0/100</div></div></div>
        <div class="join">JOIN</div>
        <svg class="felt" viewBox="0 0 300 54"><use href="#felt"/></svg>
        <div class="seat-row"><span class="seat"><svg><use href="#person"/></svg></span><span class="seat"><svg><use href="#person"/></svg></span><span class="seat"><svg><use href="#person"/></svg></span><span class="seat"><svg><use href="#person"/></svg></span><span class="seat"><svg><use href="#person"/></svg></span><span class="seat down"><svg><use href="#arrow-down"/></svg></span><span class="seat down"><svg><use href="#arrow-down"/></svg></span></div>
      </article>
      <article class="table-card">
        <div class="table-head"><div><div class="name">Baccarat A5-3C</div><div class="limit">Bet Limit</div></div><div class="right"><div class="comm">Commission 0/7</div><div class="seats">0/100</div></div></div>
        <div class="join">JOIN</div>
        <svg class="felt" viewBox="0 0 300 54"><use href="#felt"/></svg>
        <div class="seat-row"><span class="seat"><svg><use href="#person"/></svg></span><span class="seat"><svg><use href="#person"/></svg></span><span class="seat"><svg><use href="#person"/></svg></span><span class="seat"><svg><use href="#person"/></svg></span><span class="seat"><svg><use href="#person"/></svg></span><span class="seat down"><svg><use href="#arrow-down"/></svg></span><span class="seat down"><svg><use href="#arrow-down"/></svg></span></div>
      </article>
      <article class="table-card">
        <div class="table-head"><div><div class="name">Baccarat A5-3C</div><div class="limit">Bet Limit</div></div><div class="right"><div class="comm">Commission 0/7</div><div class="seats">0/100</div></div></div>
        <div class="join">JOIN</div>
        <svg class="felt" viewBox="0 0 300 54"><use href="#felt"/></svg>
        <div class="seat-row"><span class="seat"><svg><use href="#person"/></svg></span><span class="seat"><svg><use href="#person"/></svg></span><span class="seat"><svg><use href="#person"/></svg></span><span class="seat"><svg><use href="#person"/></svg></span><span class="seat"><svg><use href="#person"/></svg></span><span class="seat down"><svg><use href="#arrow-down"/></svg></span><span class="seat down"><svg><use href="#arrow-down"/></svg></span></div>
      </article>
      <article class="table-card">
        <div class="table-head"><div><div class="name">Baccarat A5-3C</div><div class="limit">Bet Limit</div></div><div class="right"><div class="comm">Commission 0/7</div><div class="seats">0/100</div></div></div>
        <div class="join">JOIN</div>
        <svg class="felt" viewBox="0 0 300 54"><use href="#felt"/></svg>
        <div class="seat-row"><span class="seat"><svg><use href="#person"/></svg></span><span class="seat"><svg><use href="#person"/></svg></span><span class="seat"><svg><use href="#person"/></svg></span><span class="seat"><svg><use href="#person"/></svg></span><span class="seat"><svg><use href="#person"/></svg></span><span class="seat down"><svg><use href="#arrow-down"/></svg></span><span class="seat down"><svg><use href="#arrow-down"/></svg></span></div>
      </article>
      <article class="table-card">
        <div class="table-head"><div><div class="name">Baccarat A5-3C</div><div class="limit">Bet Limit</div></div><div class="right"><div class="comm">Commission 0/7</div><div class="seats">0/100</div></div></div>
        <div class="join">JOIN</div>
        <svg class="felt" viewBox="0 0 300 54"><use href="#felt"/></svg>
        <div class="seat-row"><span class="seat"><svg><use href="#person"/></svg></span><span class="seat"><svg><use href="#person"/></svg></span><span class="seat"><svg><use href="#person"/></svg></span><span class="seat"><svg><use href="#person"/></svg></span><span class="seat"><svg><use href="#person"/></svg></span><span class="seat down"><svg><use href="#arrow-down"/></svg></span><span class="seat down"><svg><use href="#arrow-down"/></svg></span></div>
      </article>
    </section>
    <div class="scroll abs"><span class="scroll-thumb"></span></div>
  </main>

  <footer class="bottombar abs">
    <div class="balance abs"><span class="label">Balance</span><span class="cur">$SGD &gt;</span><span class="amount">999,999.99</span></div>
  </footer>
</div>
</body>
</html>
```